Startup Company Needs a Logo & Business Card Design

Are you creative with a great branding mentality? Our new company Amber Ridge Business Development Corp. is looking for a creative but professional logo with some WOW factor and a business card design that will get us noticed and help us kick off our brand in our market.

The logo should have two versions, a standalone logo with Amber Ridge ARD that can be used as a profile image, favicon and other locations like these. And one with the full name that would be used on print materials like the business card and website. Color and design is left to your imaginations.... It is mandatory that we will have a minimum of 2 edit sessions for small changes to the chosen design if required once the winner is selected.

We are offering a $75CDN prize to the successful designer. BUT HURRY!! Contest is only active for 3 days. Show us what you've got! The successful designer will be awarded the prize money upon submission of pint ready files in Adobe Illustrator and PNG format. There will also be the opportunity to continue design work for us as we develop our complete brand package.

Good luck to all entrants, may the best designer win. ;-)

```html
<!DOCTYPE html>
<html lang="en">
<head>
<meta charset="utf-8">
<title>Amber Ridge ARD – Business Card</title>
<link rel="stylesheet" href="https://fonts.googleapis.com/css2?family=Open+Sans:ital,wght@0,400;0,600;0,700;1,400&family=Tinos&display=swap">
<style>
  :root {
    --brand-blue: #2872b8;
    --brand-blue-light: #3a86cc;
    --slate: #58595b;
    --ink: #2b2b2b;
    --paper: #ffffff;
    --backdrop: #d9dadc;
  }
  * { box-sizing: border-box; margin: 0; padding: 0; }
  html, body {
    width: 1200px; height: 900px; overflow: hidden;
    background: var(--backdrop);
    font-family: "Open Sans", sans-serif;
  }
  .stage {
    width: 1200px; height: 900px;
    display: flex; align-items: center; justify-content: center; gap: 60px;
  }
  .card {
    position: relative;
    width: 520px; height: 300px;
    overflow: hidden;
    box-shadow: 0 6px 18px rgba(0,0,0,.18);
  }
  .card--front { background: var(--paper); }
  .card--back {
    background: var(--brand-blue);
    display: flex; align-items: center; justify-content: center;
  }

  .holder { position: absolute; left: 36px; top: 34px; }
  .holder__name { color: var(--brand-blue); font-weight: 700; font-size: 17px; letter-spacing: .2px; }
  .holder__title { color: var(--slate); font-size: 10px; font-style: italic; margin-top: 2px; }

  .contacts { position: absolute; left: 36px; top: 86px; list-style: none; }
  .contacts li {
    display: flex; align-items: center; gap: 8px;
    font-family: "Tinos", serif; font-size: 12px; color: var(--ink);
    line-height: 20px;
  }
  .contacts svg { width: 10px; height: 10px; fill: var(--brand-blue); }

  .divider {
    position: absolute; left: 36px; top: 176px;
    width: 380px; height: 1.5px; background: var(--brand-blue-light);
  }

  .wordmark { display: flex; align-items: center; gap: 8px; }
  .wordmark__dot { border-radius: 50%; background: var(--brand-blue); }
  .wordmark__name { color: var(--brand-blue); font-weight: 700; white-space: nowrap; }
  .wordmark--small { position: absolute; right: 40px; top: 92px; }
  .wordmark--small .wordmark__dot { width: 18px; height: 18px; }
  .wordmark--small .wordmark__name { font-size: 18px; }
  .wordmark--large .wordmark__dot { width: 34px; height: 34px; background: var(--paper); }
  .wordmark--large .wordmark__name { font-size: 34px; color: var(--paper); }

  .address {
    position: absolute; right: 40px; top: 190px; text-align: right;
    font-family: "Tinos", serif; font-size: 12.5px; color: var(--ink); line-height: 17px;
  }

  .footer-bands { position: absolute; left: 0; bottom: 0; width: 520px; height: 44px; }
  .website {
    position: absolute; right: 40px; bottom: 11px;
    font-family: "Tinos", serif; font-size: 13px; color: var(--paper);
  }
</style>
</head>
<body>
<main class="stage">
  <section class="card card--front" aria-label="Business card front">
    <div class="holder">
      <p class="holder__name">Melina R. Stavrou</p>
      <p class="holder__title">Notary Public LL.M.</p>
    </div>

    <ul class="contacts">
      <li><svg viewBox="0 0 10 10"><path d="M2 0h2l1 2.5-1.3 1a5.5 5.5 0 0 0 2.8 2.8l1-1.3L10 6v2c0 1-1 2-2 2A8 8 0 0 1 0 2c0-1 1-2 2-2z"/></svg>+30 210 555 0142</li>
      <li><svg viewBox="0 0 10 10"><rect x="1" y="3" width="8" height="5" rx="1"/><rect x="3" y="0.5" width="4" height="3"/></svg>+30 210 555 0187</li>
      <li><svg viewBox="0 0 10 10"><path d="M0 2h10v6H0z M0 2l5 3.5L10 2" /></svg>notary@stavrou-law.gr</li>
    </ul>

    <div class="wordmark wordmark--small">
      <span class="wordmark__dot"></span>
      <span class="wordmark__name">Amber Ridge ARD</span>
    </div>

    <div class="divider"></div>

    <address class="address" style="font-style:normal">
      14 Elm Terrace Str<br>10432 Athens Greece
    </address>

    <svg class="footer-bands" viewBox="0 0 520 44" aria-hidden="true">
      <polygon points="0,22 210,22 200,44 0,44" fill="var(--brand-blue)"/>
      <polygon points="218,6 520,6 520,44 200,44" fill="var(--slate)"/>
    </svg>
    <span class="website">www.stavrou-law.gr</span>
  </section>

  <section class="card card--back" aria-label="Business card back">
    <div class="wordmark wordmark--large">
      <span class="wordmark__dot"></span>
      <span class="wordmark__name">Amber Ridge ARD</span>
    </div>
  </section>
</main>
</body>
</html>
```